Cleaning/ butler service flyer design

We need a flyer that will be distributed through letter boxes for a small company based in Leamington Spa, called Rodrigo and Teodoro - We offer an in depth cleaning service as a one off, or regular weekly cleaning to suit the client. Rodrigo and Teodoro are experienced in hotel housekeeper services, and know the difference between what looks clean and what really is clean. We would like the designs to include green and blue colours. The flyer should also have a hint of humour but communicate trust and flexibility.

I the flyer to capitalise on the personality of these two Spanish guys doing a cleaning service.
- Logo: Use words – Rodrigo & Teodoro
o In Century Gothic Bold font
o Use a hoover to create the ‘&’ giving it the quirky logo

Rodriego & Teodoro
Cleaning at your service

I like the use of the strap line “ we know the difference between what looks clean and what really is clean”

We will provide a phone number and an email address as contact details which should appear at the bottom of the flyer.

Blue and Green colours to be used

I want the flyer to convey the fact that we don’t take our selves too seriously hence the need for humour (a bit like Ignacio in crooked gables), but the Home Cleaning Service is the main service that is offered so please use images that convey ‘Homey’ feelings.

Target Market(s)

Adults aged 36 - 55, men and women who live alone and work long hours and the last thing they want to do is clean their house on a weekend. Families with kids and or pets

Industry/Entity Type

Cleaning Service

Font styles to use
Other font styles liked:
• Century Gothic

Colors
0355a3
00a88f

Requirements
Must have
• I want to place 3 testimonials to evoke the service

```html
<!DOCTYPE html>
<html lang="en">
<head>
<meta charset="utf-8">
<title>Rodrigo &amp; Teodoro – Cleaning at your service</title>
<link rel="stylesheet" href="https://fonts.googleapis.com/css2?family=Mulish:wght@400;600;800;900&family=Dancing+Script:wght@700&display=swap">
<style>
  :root {
    --navy: #163e6e;
    --brand-blue: #0355a3;
    --teal: #00a88f;
    --script-teal: #1f5f6b;
    --leaf-green: #8cc63f;
    --bright-green: #7fbf2a;
    --body-grey: #4a5a6a;
    --paper: #ffffff;
  }
  * { margin: 0; padding: 0; box-sizing: border-box; }
  html, body { width: 1200px; height: 929px; overflow: hidden; background: var(--paper); }
  .flyer {
    position: relative;
    width: 1200px;
    height: 929px;
    background: var(--paper);
    font-family: "Mulish", "Century Gothic", sans-serif;
    color: var(--navy);
  }
  .hero-photo {
    position: absolute;
    left: 135px; top: 0;
    width: 570px; height: 490px;
    background:
      radial-gradient(ellipse at 30% 35%, #f3d77a 0%, rgba(243,215,122,0) 45%),
      radial-gradient(ellipse at 75% 55%, #f1c46a 0%, rgba(241,196,106,0) 40%),
      linear-gradient(160deg, #eef3f6 0%, #cfe0ea 40%, #6f8fae 75%, #c9d4dc 100%);
  }
  .hero-quote {
    position: absolute;
    left: 150px; top: 365px;
    width: 435px; height: 75px;
    background: var(--bright-green);
    color: var(--paper);
    font-weight: 800;
    font-size: 34px;
    display: flex; align-items: center; justify-content: center;
  }
  .strapline {
    position: absolute;
    left: 690px; top: 38px;
    width: 450px;
    text-align: center;
    font-weight: 900;
    font-size: 32px;
    line-height: 44px;
    color: var(--navy);
  }
  .strapline em {
    font-style: italic;
    color: var(--leaf-green);
  }
  .brand {
    position: absolute;
    left: 735px; top: 205px;
    width: 360px;
    display: flex; align-items: center; justify-content: center; gap: 18px;
  }
  .brand-dot {
    width: 26px; height: 26px; border-radius: 50%;
    background: var(--teal);
    flex: none;
  }
  .brand-name {
    font-weight: 900;
    font-size: 50px;
    line-height: 58px;
    color: var(--brand-blue);
    text-align: center;
  }
  .tagline {
    position: absolute;
    left: 690px; top: 465px;
    width: 450px;
    text-align: center;
    font-family: "Dancing Script", cursive;
    font-weight: 700;
    font-size: 42px;
    color: var(--script-teal);
  }
  .experience {
    position: absolute;
    left: 120px; top: 538px;
    width: 960px;
    text-align: center;
    font-weight: 800;
    font-size: 29px;
    color: var(--navy);
  }
  .services {
    position: absolute;
    left: 345px; top: 590px;
    width: 560px;
    list-style: none;
    font-size: 25px;
    line-height: 33px;
    color: var(--body-grey);
  }
  .services li {
    position: relative;
    padding-left: 22px;
    margin-bottom: 8px;
  }
  .services li::before {
    content: "";
    position: absolute;
    left: 0; top: 11px;
    width: 12px; height: 12px;
    background: var(--leaf-green);
  }
  .call-bar {
    position: absolute;
    left: 150px; top: 760px;
    width: 900px; height: 77px;
    background: var(--navy);
    color: var(--paper);
    font-weight: 800;
    font-size: 33px;
    display: flex; align-items: center; justify-content: center;
  }
  .contacts {
    position: absolute;
    left: 0; top: 858px;
    width: 1200px;
    display: flex; justify-content: center; gap: 140px;
    font-weight: 600;
    font-size: 24px;
    color: var(--navy);
  }
  .contact-item { display: flex; align-items: center; gap: 12px; }
  .contact-item svg { flex: none; }
</style>
</head>
<body>
<main class="flyer">
  <div class="hero-photo" role="img" aria-label="Photo of a young child in an apron and headscarf playfully cleaning with a spray bottle, reflected in a mirror"></div>
  <p class="hero-quote">“But mom... it’s CLEAN!”</p>

  <h1 class="strapline">We know the difference between <em>what looks clean</em> and what <em>really is clean...</em></h1>

  <div class="brand">
    <span class="brand-name">RODRIGO<br>&amp;<br>TEODORO</span>
    <span class="brand-dot"></span>
  </div>
  <p class="tagline">Cleaning at your service</p>

  <p class="experience">Rodrigo and Teodoro are experienced in hotel housekeeper services</p>
  <ul class="services">
    <li>In-depth cleaning</li>
    <li>Dog walking service available</li>
    <li>Additional services to assist in the smooth running of the household</li>
  </ul>

  <p class="call-bar">Call today for our in depth cleaning service!</p>

  <div class="contacts">
    <span class="contact-item">
      <svg width="30" height="22" viewBox="0 0 30 22" aria-hidden="true">
        <rect x="1.5" y="1.5" width="27" height="19" fill="none" stroke="var(--navy)" stroke-width="2.5"/>
        <polyline points="1.5,1.5 15,12 28.5,1.5" fill="none" stroke="var(--navy)" stroke-width="2.5"/>
      </svg>
      HELLO@TIDYHOMEMAIL.COM
    </span>
    <span class="contact-item">
      <svg width="26" height="26" viewBox="0 0 24 24" aria-hidden="true">
        <path fill="var(--navy)" d="M6.6 10.8a15.1 15.1 0 0 0 6.6 6.6l2.2-2.2a1 1 0 0 1 1-.25 11.4 11.4 0 0 0 3.6.57 1 1 0 0 1 1 1V20a1 1 0 0 1-1 1A17 17 0 0 1 3 4a1 1 0 0 1 1-1h3.5a1 1 0 0 1 1 1c0 1.25.2 2.45.57 3.57a1 1 0 0 1-.25 1z"/>
      </svg>
      555.014.2368
    </span>
  </div>
</main>
</body>
</html>
```